Wordpress Web Design & Coding for velnoragroup.ca

We need a website for a new investment company that is visually grabbing and vibrant. We would like to see a web page that displays trust, growth and confidence. Needs to be responsive and mobile friendly for all browsers and coded for both Android & IOS.

Open to the number of pages and menu items. I selected 4 but if you feel the layout would work better with less I am open to this. Need to sell the people (management team/related businesses) and then show where the invested money will be going (upcoming projects).

Company Info:

Velnora is an investment company put together by a group of seasoned business professionals who have come together to combine decades of success in the real estate development, management, financing and medical services. The company will be a full service company offering turn key solutions for medical professionals.

Vel-Nora will focus on providing a full range of services via a group of distinct companies to deliver newly emerging needs of the medical community. The end goal will be to create complete solutions for individuals in the medical community. Our group has experience and success with the conceptualization, construction and financing of medical and dental clinic spaces. Vel-Nora Group will be established to accommodate all areas of the development and creation of clinics for medical professionals from building construction to equipment financing and administrations.

You can mention these companies and take photos from their websites. You can also use stock photos.

Our construction partner:
https://382bld.com/projects/

Our equipment leasing partner:
https://www.pordiva.com/

Our Management Team and medical partners

Gil Parkes
https://www.mysoundpoise.ca/

Milos Vendraker
https://www.qrtdentalservices.com/about-us

PROPOSED PROJECTS (see attachment for details)
Hollowmere Business Park
Cresfield Business Park
Mt. Corwin Ridge Professional

Investors

Investment

Sans Serif

Must have
• Wordpress – must be both desktop and mobile friendly with fast page load speed
Ability to edit after ourselves in Wordpress
Attractive home page with logo etc.
Logo colours are: for the blue the pantone color is #0355a3
and for the green is #8cc63f

Sections, about us, what we do/services we provide, contact us

```html
<!DOCTYPE html>
<html lang="en">
<head>
<meta charset="utf-8">
<title>Vel-Nora Group</title>
<link href="https://fonts.googleapis.com/css2?family=Montserrat:wght@400;500;600;700&display=swap" rel="stylesheet">
<style>
  :root {
    --brand-blue: #0355a3;
    --brand-green: #8cc63f;
    --ink: #1f2a36;
    --white: #ffffff;
    --muted: #c9d2dc;
    --hero-deep: #1d2835;
    --hero-mid: #34465a;
    --hero-cool: #2d5b8c;
  }
  * { box-sizing: border-box; margin: 0; padding: 0; }
  html, body { width: 1200px; height: 1200px; overflow: hidden; }
  body { font-family: "Montserrat", sans-serif; background: var(--hero-deep); color: var(--white); }

  .hero { position: relative; width: 1200px; height: 820px; overflow: hidden; }
  .hero-photo {
    position: absolute; inset: 0;
    background:
      linear-gradient(180deg, rgba(20,28,38,.55) 0%, rgba(20,28,38,.25) 45%, rgba(20,28,38,.6) 100%),
      linear-gradient(100deg, var(--hero-deep) 0%, var(--hero-mid) 45%, #4a5a6a 62%, var(--hero-cool) 80%, #274d78 100%);
  }

  .site-nav {
    position: absolute; top: 26px; left: 215px; width: 770px; height: 50px;
    background: var(--white); display: flex; align-items: center; padding: 0 22px;
    color: var(--ink);
  }
  .brand { display: flex; align-items: center; gap: 8px; margin-right: 34px; }
  .brand-mark { width: 18px; height: 18px; background: var(--brand-green); }
  .brand-name { font-weight: 700; font-size: 17px; color: var(--brand-blue); letter-spacing: .2px; }
  .menu { display: flex; gap: 24px; list-style: none; font-size: 11px; font-weight: 500; }
  .menu .active { color: var(--brand-blue); }
  .lang { margin-left: auto; font-size: 10px; font-weight: 600; }
  .lang span { color: #b9c0c8; font-weight: 500; }

  .hero-copy { position: absolute; top: 240px; left: 0; width: 100%; text-align: center; }
  .hero-title { font-size: 38px; font-weight: 700; line-height: 1.2; letter-spacing: -.3px; }
  .cta {
    display: inline-block; margin-top: 44px; background: var(--brand-green); color: var(--white);
    font-size: 12px; font-weight: 700; padding: 13px 20px; text-transform: uppercase; letter-spacing: .2px;
  }

  .info-bar {
    position: absolute; bottom: 0; left: 0; width: 100%; height: 64px;
    display: flex; align-items: center; padding: 0 120px; font-size: 12px; gap: 46px;
    background: rgba(20,28,38,.35);
  }
  .info-bar strong { color: var(--brand-green); font-weight: 600; }
  .info-bar .email strong { color: var(--white); }
  .social { margin-left: auto; display: flex; align-items: center; gap: 14px; }
  .social i { width: 10px; height: 10px; border-radius: 50%; background: var(--white); display: block; }
  .social i:first-child { background: var(--brand-green); }

  .why {
    height: 380px; background: var(--brand-blue); text-align: center; padding-top: 70px;
  }
  .why-title { font-size: 20px; font-weight: 700; text-transform: uppercase; letter-spacing: 1px; }
  .why-rule { width: 50px; height: 3px; background: var(--brand-green); margin: 20px auto 34px; }
  .why-text { width: 640px; margin: 0 auto; font-size: 18px; font-weight: 500; line-height: 1.6; color: #e8eef6; }
</style>
</head>
<body>
  <header class="hero">
    <div class="hero-photo" role="img" aria-label="Photo of a bright medical clinic office with a staff member at a desk, blue window blinds behind"></div>

    <nav class="site-nav">
      <div class="brand"><span class="brand-mark"></span><span class="brand-name">VEL-NORA GROUP</span></div>
      <ul class="menu">
        <li class="active">Home</li>
        <li>About Us</li>
        <li>What we do</li>
        <li>Solutions</li>
        <li>Contact us</li>
      </ul>
      <div class="lang">ENG <span>| FRA</span></div>
    </nav>

    <div class="hero-copy">
      <h1 class="hero-title">To assist the medical<br>community in catering<br>to those services</h1>
      <a class="cta">Enquire now!</a>
    </div>

    <div class="info-bar">
      <div class="email">Email: <strong>hello@velnora-group.com</strong></div>
      <div>Phone: <strong>(+012) 555-0148-20</strong></div>
      <div class="social">Follow us: <i></i><i></i><i></i><i></i><i></i></div>
    </div>
  </header>

  <section class="why">
    <h2 class="why-title">Why choose Vel-Nora</h2>
    <div class="why-rule"></div>
    <p class="why-text">We are a group of seasoned business professionals who have come together to combine decades of success in the real estate development.</p>
  </section>
</body>
</html>
```